Frostvale Climate Services WA Truck

I want a truck desing that screams Professional, Friendly and serious about work. you can find some of our work on our website, facebook and instagram.
https://frostvaleclimate.com.au/
https://www.instagram.com/frstvlhvac/
https://www.facebook.com/profile.php?id=73829106548213

The design needs to include our refrigeration license: AU47325 and electrical License: EC58913
I want the colours to be consistent with my Logo.

Key Notes to be included in the design, I want to let people know we do the following;
- Commercial and Residential
- Repairs, Service and Installation
- Reverse cycle ducted Air Conditioning
- Wall Split Air Conditioning
- Ceiling Cassettes
- Evaporative Air Conditioning
- Cool Rooms
- Display Fridges
- Beer Chillers

```html
<!DOCTYPE html>
<html lang="en">
<head>
<meta charset="utf-8">
<title>Frostvale Climate Services WA – Truck Graphics</title>
<link rel="stylesheet" href="https://fonts.googleapis.com/css2?family=Oswald:wght@300;400;500&family=Open+Sans:wght@400&display=swap">
<style>
  :root {
    --navy: #1a2860;
    --navy-deep: #131d4a;
    --blue: #1757a8;
    --orange: #f2611e;
    --gold: #f7b335;
    --white: #ffffff;
    --soft: #e6eaf4;
    --photo-dark: #1d2233;
    --photo-mid: #30394d;
  }
  * { box-sizing: border-box; margin: 0; padding: 0; }
  html, body { width: 1200px; height: 855px; overflow: hidden; background: var(--white); }
  .canvas { position: relative; width: 1200px; height: 855px; overflow: hidden; background: var(--white); }

  /* ---------- shared brand block ---------- */
  .brand-name {
    font-family: "Oswald", sans-serif; font-weight: 500; color: var(--gold);
    text-transform: uppercase; line-height: 1.1; letter-spacing: 0.06em;
  }
  .brand-name small { display: block; font-size: 0.5em; letter-spacing: 0.18em; }
  .brand-mark {
    display: block; margin: 0 auto 8px; border-radius: 50%; background: var(--orange);
  }

  /* ---------- rear door panel ---------- */
  .rear-panel {
    position: absolute; left: 30px; top: 256px; width: 371px; height: 343px;
    background: linear-gradient(160deg, var(--navy) 0%, var(--navy) 45%, var(--blue) 100%);
    color: var(--white); text-align: center; overflow: hidden;
  }
  .rear-panel .brand { position: absolute; left: 0; right: 0; top: 18px; }
  .rear-panel .brand-mark { width: 40px; height: 40px; }
  .rear-panel .brand-name { font-size: 28px; }

  .licences { position: absolute; left: 0; right: 0; top: 148px; display: flex; justify-content: center; }
  .licence { padding: 0 12px; text-align: left; }
  .licence + .licence { border-left: 2px solid var(--orange); }
  .licence-label { font-family: "Open Sans", sans-serif; font-size: 14px; color: var(--soft); line-height: 1.2; }
  .licence-number { font-family: "Oswald", sans-serif; font-weight: 400; font-size: 42px; line-height: 1.05; }

  .rear-rule {
    position: absolute; left: 63px; width: 245px; top: 224px; height: 1px;
    background: linear-gradient(90deg, transparent, var(--gold), transparent);
  }
  .cta { position: absolute; left: 0; right: 0; top: 230px; font-family: "Oswald", sans-serif; font-weight: 300; font-size: 20px; }
  .rear-panel .phone { position: absolute; left: 0; right: 0; top: 254px; font-family: "Oswald", sans-serif; font-weight: 500; font-size: 52px; line-height: 1.1; }

  /* ---------- side panel ---------- */
  .side-panel {
    position: absolute; left: 441px; top: 258px; width: 730px; height: 339px;
    background: linear-gradient(100deg, var(--navy) 0%, var(--navy) 40%, var(--blue) 70%);
    color: var(--white); overflow: hidden;
  }
  .side-art { position: absolute; inset: 0; width: 100%; height: 100%; }

  .service-list { position: absolute; left: 28px; top: 13px; list-style: none; }
  .service-list li {
    display: flex; align-items: center; height: 33.8px;
    font-family: "Oswald", sans-serif; font-weight: 300; font-size: 20px; white-space: nowrap;
  }
  .tick { width: 20px; height: 16px; margin-right: 11px; flex: none; }

  .side-panel .brand { position: absolute; left: 470px; width: 230px; top: 40px; text-align: center; }
  .side-panel .brand-mark { width: 40px; height: 40px; }
  .side-panel .brand-name { font-size: 30px; }

  .side-licences { position: absolute; left: 272px; top: 237px; font-family: "Oswald", sans-serif; font-weight: 400; font-size: 24px; line-height: 1; }
  .side-licences .divider { display: inline-block; width: 2px; height: 22px; background: var(--orange); margin: 0 6px; vertical-align: -3px; }
  .side-panel .phone { position: absolute; left: 226px; top: 260px; font-family: "Oswald", sans-serif; font-weight: 500; font-size: 49px; line-height: 1.1; }
</style>
</head>
<body>
<main class="canvas">

  <section class="rear-panel" aria-label="Rear door graphic">
    <div class="brand">
      <span class="brand-mark"></span>
      <p class="brand-name">Frostvale<small>Climate Services WA</small></p>
    </div>
    <div class="licences">
      <div class="licence">
        <p class="licence-label">refrigeration license</p>
        <p class="licence-number">AU47325</p>
      </div>
      <div class="licence">
        <p class="licence-label">electrical License</p>
        <p class="licence-number">EC58913</p>
      </div>
    </div>
    <div class="rear-rule"></div>
    <p class="cta">call today for an estimate</p>
    <p class="phone">0491 570 156</p>
  </section>

  <section class="side-panel" aria-label="Side body graphic">
    <svg class="side-art" viewBox="0 0 1045 485" preserveAspectRatio="none">
      <defs>
        <linearGradient id="swoopGrad" x1="0" y1="0" x2="1" y2="1">
          <stop offset="0" stop-color="#f7b335"/>
          <stop offset="0.55" stop-color="#f59a2c"/>
          <stop offset="1" stop-color="#f2611e"/>
        </linearGradient>
        <linearGradient id="photoGrad" x1="0" y1="0" x2="1" y2="1">
          <stop offset="0" stop-color="#30394d"/>
          <stop offset="1" stop-color="#1d2233"/>
        </linearGradient>
      </defs>
      <path role="img" aria-label="Photo of a technician servicing outdoor air conditioning units"
            d="M580,0 C600,250 820,400 1045,410 L1045,0 Z" fill="url(#photoGrad)"/>
      <path d="M555,0 C565,300 800,470 1045,485 L1045,410 C820,400 600,250 580,0 Z" fill="url(#swoopGrad)"/>
    </svg>

    <ul class="service-list">
      <li><svg class="tick" viewBox="0 0 20 16"><path d="M2 8 L8 14 L18 2" fill="none" stroke="#f2611e" stroke-width="2.4" stroke-linecap="round" stroke-linejoin="round"/></svg>Commercial and Residential</li>
      <li><svg class="tick" viewBox="0 0 20 16"><path d="M2 8 L8 14 L18 2" fill="none" stroke="#f2611e" stroke-width="2.4" stroke-linecap="round" stroke-linejoin="round"/></svg>Repairs, Service and Installation</li>
      <li><svg class="tick" viewBox="0 0 20 16"><path d="M2 8 L8 14 L18 2" fill="none" stroke="#f2611e" stroke-width="2.4" stroke-linecap="round" stroke-linejoin="round"/></svg>Reverse cycle ducted Air Conditioning</li>
      <li><svg class="tick" viewBox="0 0 20 16"><path d="M2 8 L8 14 L18 2" fill="none" stroke="#f2611e" stroke-width="2.4" stroke-linecap="round" stroke-linejoin="round"/></svg>Wall Split Air Conditioning</li>
      <li><svg class="tick" viewBox="0 0 20 16"><path d="M2 8 L8 14 L18 2" fill="none" stroke="#f2611e" stroke-width="2.4" stroke-linecap="round" stroke-linejoin="round"/></svg>Ceiling Cassettes</li>
      <li><svg class="tick" viewBox="0 0 20 16"><path d="M2 8 L8 14 L18 2" fill="none" stroke="#f2611e" stroke-width="2.4" stroke-linecap="round" stroke-linejoin="round"/></svg>Evaporative Air Conditioning</li>
      <li><svg class="tick" viewBox="0 0 20 16"><path d="M2 8 L8 14 L18 2" fill="none" stroke="#f2611e" stroke-width="2.4" stroke-linecap="round" stroke-linejoin="round"/></svg>Cool Rooms</li>
      <li><svg class="tick" viewBox="0 0 20 16"><path d="M2 8 L8 14 L18 2" fill="none" stroke="#f2611e" stroke-width="2.4" stroke-linecap="round" stroke-linejoin="round"/></svg>Display Fridges</li>
      <li><svg class="tick" viewBox="0 0 20 16"><path d="M2 8 L8 14 L18 2" fill="none" stroke="#f2611e" stroke-width="2.4" stroke-linecap="round" stroke-linejoin="round"/></svg>Beer Chillers</li>
    </ul>

    <div class="brand">
      <span class="brand-mark"></span>
      <p class="brand-name">Frostvale<small>Climate Services WA</small></p>
    </div>

    <p class="side-licences">AU47325<span class="divider"></span>EC58913</p>
    <p class="phone">0491 570 156</p>
  </section>

</main>
</body>
</html>
```